MARLOWE BRIGHT WORKS WEBSITE HOME PAGE AND CHECKOUT PAGES

UPDATE TO BRIEF:

Marlowe Bright Works is a company that provides Charities with the Free Vacation Vouchers that they can use to incentivize people to donate which in turn increases donations for the chairty.

So I need to keep it a little more template like the example url I gave. http://pagefernly.com/marlowe-bright-work/ Because, I am going to provide template to ANY CHARITY TYPE and they just fill in the content into the template and change images or whatever for their charity. So I am really looking for a website template that can be used for multiple and different kinds of charities.

So where the logo would go please use YOUR LOGO HERE generic logo for now

and where ever you promote the Free Vacation Certificate To Las Vegas please add "Brought To You By" (logo marlowe bright works or something...basically its a partnership with the Charity and Marlowe Bright Work)

So Marlowe Bright Work is a marketing company and not a Charity but more of a plug and play platform that allows a charity to accepts donations and immediately deliver the promised incentive offer after donation is made on the website.

When a Charity is able to offer a high perceived value gift for a donation they increase donations.

Target Market(s)

PEOPLE THAT DONATE TO CHARITIES

Industry/Entity Type

Charity

Number of Pages Required

3 page

Requirements
Must have
• One thing i need to add to the website is an Incentive Gift for the Donation.

So I need this tagline and images to make the promotion seem great:
"Donate $100 and Receive A Free 3 Night Vacation Certificate To Las Vegas!"

Maybe show image of vegas or some kind of nice graphic that promotes the vegas vacation as a gift for the $100 donation very well"

I need the payment pages as well. So when someone click Donate Now, the next page is there where they can see their gift that is included with the donation, and also the donation amount...
Nice to have

Should not have

```html
<!DOCTYPE html>
<html lang="en">
<head>
<meta charset="utf-8">
<title>Marlowe Bright Works – Donate</title>
<link rel="stylesheet" href="https://fonts.googleapis.com/css2?family=Poppins:wght@400;500;600;700&display=swap">
<style>
  :root{
    --stage:#707070;
    --paper:#f1f1f1;
    --sky-top:#0a86ff;
    --sky-bottom:#1e90f0;
    --royal:#0a6cf0;
    --navy:#003a9e;
    --navy-deep:#00359a;
    --ink:#0d3a8c;
    --white:#ffffff;
    --muted:#c4c4c4;
    --pale:#a9d3f2;
    --accent:#1ec8e0;
    --photo-a:#3ea0ec;
    --photo-b:#e9eef5;
    --photo-c:#5b8f3a;
  }
  *{box-sizing:border-box;margin:0;padding:0}
  html,body{width:1200px;height:1000px;overflow:hidden;background:var(--stage);font-family:"Poppins",sans-serif}
  .canvas{position:relative;width:1200px;height:1000px;overflow:hidden}
  .page{position:absolute;left:344px;top:0;width:895px;height:1750px;transform:scale(0.5714);transform-origin:0 0;background:var(--paper);overflow:hidden}
  .abs{position:absolute}

  /* header */
  .site-header{left:0;top:0;width:895px;height:88px;background:var(--paper)}
  .logo-placeholder{left:196px;top:34px;font-size:20px;font-weight:700;color:var(--ink);letter-spacing:.5px}
  .contact{left:590px;top:36px;font-size:9px;font-weight:600;color:var(--ink);line-height:15px}
  .contact-row{display:flex;align-items:center;gap:6px}

  /* hero */
  .hero{left:0;top:88px;width:895px;height:969px;background:linear-gradient(180deg,var(--sky-top),var(--sky-bottom) 55%,var(--royal))}
  .hero-photo{left:340px;top:120px;width:555px;height:500px;background:radial-gradient(ellipse at 60% 45%,var(--photo-b) 0 22%,transparent 45%),linear-gradient(180deg,var(--photo-a) 0%,#4aa6ee 55%,var(--photo-c) 100%);border-radius:0 0 0 120px}
  .hero-copy{left:204px;top:180px;color:var(--white);line-height:1.15}
  .hero-copy .small{font-size:20px;font-weight:500}
  .hero-copy .amount{font-size:28px;font-weight:600}
  .hero-copy .big{font-size:30px;font-weight:600;margin:4px 0}
  .btn-outline{border:2px solid var(--white);border-radius:14px;color:var(--white);font-size:9px;font-weight:600;text-align:center;line-height:22px}
  .hero-cta{left:202px;top:330px;width:102px;height:26px}
  .sponsor-card{left:202px;top:548px;width:218px;height:104px;background:var(--white);padding:28px 18px}
  .sponsor-card .label{font-size:8px;color:#333;font-weight:500}
  .sponsor-name{display:flex;align-items:center;gap:8px;margin-top:16px;font-size:15px;font-weight:600;color:var(--navy)}
  .sponsor-name .mark{width:16px;height:16px;background:var(--accent)}

  .goal-title{left:0;width:895px;top:690px;text-align:center;color:var(--white)}
  .goal-title h2{font-size:30px;font-weight:600;line-height:1.1}
  .goal-title p{font-size:19px;font-weight:500}
  .goal-title strong{font-size:28px;font-weight:600}
  .progress{left:282px;top:786px;width:333px;height:52px;border-radius:26px;background:var(--white);border:2px solid var(--navy);overflow:hidden}
  .progress-fill{height:100%;width:112px;background:var(--navy)}
  .progress-label{top:848px;font-size:9px;font-weight:600;color:var(--white)}

  /* checkout */
  .checkout{left:0;top:1130px;width:895px;height:620px;background:var(--pale)}
  .checkout-photo{left:640px;top:160px;width:255px;height:420px;background:linear-gradient(180deg,#c9e4f6,#f4e7c8 60%,#b9d7a4);opacity:.8}
  .donation-form{left:204px;top:1151px;width:486px;height:484px;background:var(--navy-deep);color:var(--white);text-align:center}
  .donation-form h3{position:absolute;left:0;width:100%;font-size:22px;font-weight:600}
  .amount-field{left:88px;top:75px;width:307px;height:48px;border-radius:24px;background:var(--white);color:var(--muted);font-size:28px;font-weight:500;line-height:48px}
  .field{height:24px;border-radius:12px;background:var(--white);color:var(--navy);font-size:8px;font-weight:600;text-align:left;padding-left:15px;line-height:24px}
  .field.select::after{content:"";position:absolute;right:14px;top:10px;border:4px solid transparent;border-top-color:var(--navy)}
  .pay-option{width:89px;height:48px;border-radius:24px;background:var(--white);color:var(--navy);font-size:8px;font-weight:600;display:flex;flex-direction:column;align-items:center;justify-content:center;gap:3px;top:363px}
  .submit{left:192px;top:429px;width:102px;height:26px}
</style>
</head>
<body>
<div class="canvas">
  <div class="page">
    <header class="site-header abs">
      <div class="logo-placeholder abs">Your Logo Here</div>
      <div class="contact abs">
        <div class="contact-row"><svg width="8" height="12" viewBox="0 0 8 12"><rect x="1" y="0.5" width="6" height="11" rx="1" fill="none" stroke="#0d3a8c" stroke-width="1.2"/></svg>0100200300</div>
        <div class="contact-row"><svg width="10" height="8" viewBox="0 0 10 8"><rect x="0.5" y="0.5" width="9" height="7" fill="#0d3a8c"/><path d="M0.5 0.5 5 4.5 9.5 0.5" fill="none" stroke="#fff"/></svg>info@marlowebrightworks</div>
      </div>
    </header>

    <section class="hero abs">
      <div class="hero-photo abs" role="img" aria-label="Photo of the Las Vegas welcome sign with palm trees against a blue sky"></div>
      <svg class="abs" style="left:0;top:430px" width="895" height="539" viewBox="0 0 895 539">
        <path d="M0 10 C60 80 140 120 220 110 C330 95 430 40 560 40 C700 40 800 110 895 80 L895 539 L0 539Z" fill="#0a6cf0"/>
        <path d="M540 40 C680 30 800 100 895 70 L895 135 C820 150 720 70 560 50Z" fill="#003a9e"/>
        <path d="M0 380 C120 330 210 420 380 420 C560 420 700 330 895 400 L895 539 L0 539Z" fill="#003a9e"/>
      </svg>
      <div class="sponsor-card abs" style="top:460px">
        <div class="label">Brought To You By</div>
        <div class="sponsor-name"><span class="mark"></span>Marlowe Bright Works</div>
      </div>
    </section>

    <div class="hero-copy abs">
      <div class="small">Donate <span class="amount">$100</span> and get a</div>
      <div class="big">Free 3 Night Vacation</div>
      <div class="small">certificate for</div>
      <div class="big">Las Vegas!</div>
    </div>
    <div class="btn-outline hero-cta abs">DONATE NOW</div>

    <div class="goal-title abs">
      <h2>Donate today</h2>
      <p>&amp; help us reach our <strong>$1M goal</strong></p>
    </div>
    <div class="progress abs"><div class="progress-fill"></div></div>
    <div class="progress-label abs" style="left:284px">$ 00.00</div>
    <div class="progress-label abs" style="left:563px">$1,000,000</div>

    <section class="checkout abs">
      <div class="checkout-photo abs" role="img" aria-label="Faded photo of the Las Vegas welcome sign"></div>
      <svg class="abs" style="left:0;top:400px" width="895" height="220" viewBox="0 0 895 220">
        <path d="M0 40 C80 110 180 140 320 130 C480 120 600 70 700 90 C800 110 850 160 895 150 L895 220 L0 220Z" fill="#f1f1f1"/>
      </svg>
    </section>

    <form class="donation-form abs">
      <h3 style="top:22px">Donation Amount</h3>
      <div class="amount-field abs">$ 1.00</div>
      <h3 style="top:140px">Personal Details</h3>
      <div class="field abs" style="left:88px;top:184px;width:151px">First Name*</div>
      <div class="field abs" style="left:246px;top:184px;width:151px">Last Name*</div>
      <div class="field abs" style="left:88px;top:218px;width:151px">Email*</div>
      <div class="field abs" style="left:246px;top:218px;width:151px">Phone Number*</div>
      <div class="field abs" style="left:88px;top:253px;width:151px">Address*</div>
      <div class="field select abs" style="left:246px;top:253px;width:151px">Country</div>
      <div class="field abs" style="left:88px;top:287px;width:309px">Note</div>
      <h3 style="top:324px">Payment Option</h3>
      <div class="pay-option abs" style="left:88px">
        <svg width="26" height="16" viewBox="0 0 26 16"><rect x="1" y="1" width="24" height="14" rx="2" fill="none" stroke="#003a9e" stroke-width="1.5"/><line x1="1" y1="5" x2="25" y2="5" stroke="#003a9e" stroke-width="2"/><circle cx="20" cy="11" r="1.6" fill="none" stroke="#003a9e"/></svg>Credit Card</div>
      <div class="pay-option abs" style="left:198px">
        <svg width="26" height="16" viewBox="0 0 26 16"><rect x="1" y="1" width="24" height="14" rx="2" fill="none" stroke="#003a9e" stroke-width="1.5"/><line x1="4" y1="9" x2="12" y2="9" stroke="#003a9e"/><rect x="17" y="7" width="5" height="4" fill="#003a9e"/></svg>Debit Card</div>
      <div class="pay-option abs" style="left:308px">
        <svg width="22" height="18" viewBox="0 0 22 18"><rect x="1" y="5" width="20" height="12" rx="2" fill="none" stroke="#003a9e" stroke-width="1.5"/><path d="M4 5 13 1 15 5" fill="none" stroke="#003a9e" stroke-width="1.5"/><rect x="15" y="9" width="6" height="4" fill="#003a9e"/></svg>Wallet</div>
      <div class="btn-outline submit abs">SUBMIT</div>
    </form>
  </div>
</div>
</body>
</html>
```